Belcotti Business Cards

Business cards for real estate
Target Market(s)
Real estate
Industry/Entity Type
Real Estate Agent
Font styles to use
Serif
Requirements
Must have
- Photo and logo

```html
<!DOCTYPE html>
<html lang="en">
<head>
<meta charset="utf-8">
<title>Belcotti Realty – Business Cards</title>
<link rel="stylesheet" href="https://fonts.googleapis.com/css2?family=Libre+Baskerville:wght@400;700&display=swap">
<style>
  :root {
    --bg: #e4e4e4;
    --card: #ffffff;
    --ink: #1c1c1c;
    --muted: #444444;
    --brand-red: #8a1f2c;
    --brand-gold: #c49a5a;
    --rule: #bdbdbd;
    --band-dark: #141414;
    --photo-top: #d9d6d2;
    --photo-bottom: #2a2f3a;
  }
  * { box-sizing: border-box; margin: 0; padding: 0; }
  html, body { width: 1200px; height: 880px; overflow: hidden; }
  body {
    background: var(--bg);
    font-family: "Libre Baskerville", Georgia, serif;
    color: var(--ink);
    position: relative;
  }
  .card {
    position: absolute;
    left: 270px;
    width: 660px;
    height: 377px;
    background: var(--card);
    border-radius: 22px;
    overflow: hidden;
    box-shadow: 0 8px 24px rgba(0,0,0,0.18);
  }
  .card--front { top: 40px; }
  .card--back { top: 463px; }

  .brand {
    position: absolute;
    display: flex;
    align-items: center;
    gap: 16px;
  }
  .brand__mark {
    border-radius: 50%;
    background: var(--brand-red);
    flex: none;
  }
  .brand__name {
    color: var(--ink);
    font-weight: 400;
    letter-spacing: 0.12em;
    line-height: 1.15;
    text-transform: uppercase;
  }
  .card--front .brand { left: 50%; top: 50%; transform: translate(-50%, -50%); }
  .card--front .brand__mark { width: 78px; height: 78px; }
  .card--front .brand__name { font-size: 34px; }

  .card--back .brand { left: 360px; top: 40px; }
  .card--back .brand__mark { width: 62px; height: 62px; }
  .card--back .brand__name { font-size: 27px; }

  .agent-photo {
    position: absolute;
    left: 70px;
    top: 112px;
    width: 300px;
    height: 265px;
    background: linear-gradient(180deg, var(--photo-top) 0%, var(--photo-bottom) 75%);
    border-radius: 120px 120px 0 0;
  }

  .agent {
    position: absolute;
    left: 360px;
    top: 130px;
    width: 270px;
  }
  .agent__title {
    font-size: 16px;
    letter-spacing: 0.04em;
    padding-bottom: 8px;
    border-bottom: 1px solid var(--rule);
    margin-bottom: 10px;
  }
  .agent__name { text-transform: uppercase; }
  .agent__sep { color: var(--rule); margin: 0 6px; }
  .agent__role { color: var(--brand-red); font-size: 14px; }
  .agent__address { font-size: 12px; line-height: 1.5; color: var(--muted); margin-bottom: 6px; }
  .contact { list-style: none; font-size: 12px; color: var(--muted); }
  .contact__item { display: flex; align-items: center; gap: 8px; margin-bottom: 5px; }
  .contact__icon { width: 18px; height: 18px; flex: none; }

  .footer-bands { position: absolute; left: 0; bottom: 0; width: 660px; height: 48px; }
  .website {
    position: absolute;
    left: 90px;
    bottom: 12px;
    color: #ffffff;
    font-size: 13px;
    letter-spacing: 0.03em;
  }
</style>
</head>
<body>

  <section class="card card--front" aria-label="Card front">
    <div class="brand">
      <span class="brand__mark"></span>
      <span class="brand__name">Belcotti<br>Realty</span>
    </div>
  </section>

  <section class="card card--back" aria-label="Card back">
    <div class="brand">
      <span class="brand__mark"></span>
      <span class="brand__name">Belcotti<br>Realty</span>
    </div>

    <div class="agent-photo" role="img" aria-label="Portrait photo of the agent in a dark suit and blue tie"></div>

    <div class="agent">
      <p class="agent__title"><span class="agent__name">Marco Delane</span><span class="agent__sep">|</span><span class="agent__role">Realtor</span></p>
      <p class="agent__address">PO Box 418, Harbour Lane<br>7 Westgate Road, Carrow</p>
      <ul class="contact">
        <li class="contact__item">
          <svg class="contact__icon" viewBox="0 0 18 18" aria-hidden="true">
            <circle cx="9" cy="9" r="8" fill="none" stroke="var(--brand-gold)" stroke-width="1.5"/>
            <rect x="6" y="4.5" width="6" height="9" rx="1" fill="none" stroke="var(--brand-red)" stroke-width="1.3"/>
          </svg>
          <span>(555) 218 4470</span>
        </li>
        <li class="contact__item">
          <svg class="contact__icon" viewBox="0 0 18 18" aria-hidden="true">
            <circle cx="9" cy="9" r="8" fill="none" stroke="var(--brand-gold)" stroke-width="1.5"/>
            <rect x="4.5" y="6" width="9" height="6" fill="var(--brand-red)"/>
            <path d="M4.5 6 L9 9.5 L13.5 6" fill="none" stroke="#fff" stroke-width="0.9"/>
          </svg>
          <span>hello@belcottirealty.com</span>
        </li>
      </ul>
    </div>

    <svg class="footer-bands" viewBox="0 0 660 48" aria-hidden="true">
      <polygon points="395,24 660,24 660,48 395,48" fill="var(--band-dark)"/>
      <polygon points="0,6 400,6 420,48 0,48" fill="var(--brand-red)"/>
    </svg>
    <p class="website">www.belcottirealty.com</p>
  </section>

</body>
</html>
```